Short Line Railroad website - small company simple homepage

We are looking for someone to design a webpage/home page for our railroad. Doesn't have to be fancy, just basic contact info and links to our regional partners and government agencies. We don't do any online sales but would like a web presence that makes us look professional. We have a logo, and some pictures, but are open to purchasing pictures or other graphical elements to enhance this site. We would like links to our partners websites and emergency information. I don't know how many pages this will take??

Target Market(s)

The website is for our existing customers and their partners, potential new rail customers, regional partners like Ports or Economic Development Agencies, and government regulators. We also need emergency contact info and instructions for the general public.

Industry/Entity Type

It Company

Coding

Coded - Design and coding required

Number of Pages Required

2 page

Font styles to use
Sans Serif

Requirements
Must have
• Our logo - map of railroad and area - some photos - contact info - links to designated partners - emergency contact info and emergency instructions.
• Partners include Fenwick County Washington
• Port of Merriton (Washington)
• LNPGA
• City of Hollow Brook
• National Trackway Bureau
• MBQ
• KPLTR
• will add more when I have time
Nice to have
• It would be nice to mostly use our company colors - red, black, and white.
• Just a very professional looking website, with the option of making changes in house in the future.
Should not have
• No ads

```html
<!DOCTYPE html>
<html lang="en">
<head>
<meta charset="utf-8">
<title>Harlow Ridge Junction Railroad</title>
<link href="https://fonts.googleapis.com/css2?family=Open+Sans:ital,wght@0,400;0,600;0,700;1,400&display=swap" rel="stylesheet">
<style>
:root{
  --red:#e8252f;
  --red-dark:#c81820;
  --red-light:#f5464e;
  --ink:#222;
  --text:#444;
  --muted:#666;
  --line:#e3e3e3;
  --white:#fff;
}
*{box-sizing:border-box;margin:0;padding:0}
html,body{width:1200px;height:2844px;overflow:hidden}
body{font-family:"Open Sans",Arial,sans-serif;color:var(--text);background:var(--white);position:relative}
.wrap{width:1002px;margin:0 auto;position:relative}
.btn{display:inline-block;background:linear-gradient(var(--red-light),var(--red-dark));color:var(--white);font-size:15px;padding:10px 18px;border-radius:3px;text-decoration:none}
.btn-sm{font-size:14px;padding:6px 12px;border-radius:2px}
.section-title{font-size:27px;font-weight:700;color:#333}

/* header */
.site-header{height:110px}
.site-header .wrap{height:110px;display:flex;align-items:center}
.brand{display:flex;align-items:center;gap:6px;text-decoration:none}
.brand-mark{width:70px;height:70px;background:var(--red);flex:none}
.brand-name{font-size:20px;font-weight:700;color:var(--red);line-height:1.3}
.tagline{margin-left:120px;font-size:20px;font-style:italic;color:#555}
.call{margin-left:auto;display:flex;align-items:center;gap:14px}
.call-label{font-size:17px;color:#333;line-height:1.2}
.call-number{font-size:22px;font-weight:700;color:#222}

/* nav */
.main-nav{height:57px;background:linear-gradient(var(--red-light),var(--red-dark))}
.main-nav ul{list-style:none;display:flex;width:1002px;margin:0 auto;height:57px}
.main-nav li{flex:1;text-align:center;line-height:57px;font-size:12px;color:var(--white);text-transform:uppercase;border-left:1px solid rgba(255,255,255,.25)}
.main-nav li:first-child{border-left:0}

/* hero */
.hero{height:535px;position:relative;background:linear-gradient(160deg,#6f7a6a 0%,#5b6a4f 35%,#3c4434 70%,#2c3128 100%)}
.hero-copy{position:absolute;left:99px;top:155px;width:660px;color:var(--white)}
.hero-copy h1{font-size:40px;font-weight:700;margin-bottom:14px}
.hero-copy p{font-size:16px;line-height:1.5;margin-bottom:24px}
.hero-arrow{position:absolute;top:205px;width:46px;height:46px;border-radius:50%;background:rgba(255,255,255,.45);display:flex;align-items:center;justify-content:center}

/* welcome */
.welcome{height:299px;border-bottom:1px solid var(--line)}
.welcome .wrap{display:flex;padding-top:28px}
.welcome-copy{width:700px}
.welcome-copy h2{font-size:27px;font-weight:700;color:var(--red);margin-bottom:12px}
.welcome-copy .lead{font-size:16px;color:#333;margin-bottom:14px}
.welcome-copy p{font-size:12.5px;line-height:1.75;margin-bottom:18px}
.welcome-photo{margin-left:auto;width:272px;height:220px;border:6px solid var(--white);box-shadow:0 1px 6px rgba(0,0,0,.35);background:linear-gradient(180deg,#aac3d6 0%,#8aa06f 55%,#5b7240 100%)}

/* services */
.services{height:503px;border-bottom:1px solid var(--line)}
.services .wrap{padding-top:38px}
.slide-toggle{position:absolute;right:0;top:44px;width:46px;height:46px;border-radius:50%;border:1px solid #ddd;box-shadow:0 1px 3px rgba(0,0,0,.2)}
.service-grid{display:flex;gap:14px;margin-top:34px}
.service-card{width:240px;height:356px;border:1px solid var(--line);padding:3px}
.service-photo{height:167px}
.service-card h3{font-size:18px;font-weight:400;color:var(--red);margin:20px 16px 10px}
.service-card p{font-size:12.5px;line-height:1.6;margin:0 16px 14px;color:#555}
.service-card .btn{margin-left:16px}

/* emergency + gallery */
.info-row{height:411px}
.info-row .wrap{display:flex;padding-top:26px}
.emergency{width:536px;padding-right:30px;border-right:1px solid var(--line);height:355px}
.gallery{padding-left:32px;flex:1}
.info-row h2{font-size:27px;font-weight:700;color:#333;margin-bottom:10px}
.info-row .intro{font-size:13.5px;color:var(--red);line-height:1.6;margin-bottom:26px}
.emergency-body{display:flex;gap:20px}
.emergency-illustration{width:300px;height:222px;flex:none;border:5px solid var(--white);box-shadow:0 1px 6px rgba(0,0,0,.35);background:linear-gradient(135deg,#f6e6a0 0%,#f3d765 60%,#e6c24a 100%)}
.emergency-body p{font-size:12.5px;line-height:1.6;margin-bottom:16px;color:#555}
.gallery-grid{display:grid;grid-template-columns:repeat(3,1fr);gap:3px;width:433px;height:258px}
.gallery-grid span{display:block}

/* map */
.map-band{height:421px;position:relative;background:radial-gradient(ellipse at 50% 50%,#6f7d46 0%,#5d6a3a 45%,#6b6b66 75%,#55554f 100%)}
.map-link{position:absolute;left:0;right:0;top:134px;text-align:center;color:var(--white);font-size:20px}
.map-link .pin{width:66px;height:66px;border-radius:50%;border:2px solid rgba(255,255,255,.6);margin:0 auto 20px;display:flex;align-items:center;justify-content:center}

/* partners */
.partners{height:191px;text-align:center}
.partners .section-title{padding-top:18px}
.partner-row{display:flex;justify-content:space-between;align-items:center;width:1002px;margin:34px auto 0;position:relative}
.partner{width:72px;height:72px;border-radius:50%;background:#cfd6e2}
.partner.square{border-radius:6px;width:150px;height:56px;background:#d6d9de}
.partner-arrow{position:absolute;top:26px;color:#aaa;font-size:22px}

/* footer */
.site-footer{height:251px;background:linear-gradient(var(--red-light),var(--red))}
.site-footer .wrap{display:grid;grid-template-columns:182px 320px 262px 1fr;padding-top:34px;color:var(--white)}
.site-footer h4{font-size:12.5px;font-weight:700;text-transform:uppercase;margin-bottom:18px;display:flex;align-items:center;gap:8px}
.site-footer ul{list-style:none}
.site-footer li{font-size:12px;line-height:28.5px}
.field{width:210px;height:30px;background:var(--white);font-size:11px;color:#aaa;padding:7px 12px;margin-bottom:12px}
.submit{width:128px;height:40px;border:1px solid rgba(255,255,255,.8);border-radius:3px;font-size:14px;text-align:center;line-height:38px;margin-top:10px}
.socials{display:flex;gap:8px}
.socials span{width:36px;height:36px;border-radius:50%;border:2px solid rgba(255,255,255,.85)}
.socials span:nth-child(1){background:#3b5b9e}
.socials span:nth-child(2){background:#2ea2e0}
.socials span:nth-child(3){background:#c4302b}
.socials span:nth-child(4){background:#a52a2a}
.socials span:nth-child(5){background:#c79a20}
.contact li{display:flex;gap:10px;line-height:1.9}
.contact b{font-weight:700}
.copyright{height:66px;background:var(--red);border-top:1px solid rgba(255,255,255,.2);text-align:center;line-height:66px;color:var(--white);font-size:11px;text-transform:uppercase}
</style>
</head>
<body>

<header class="site-header">
  <div class="wrap">
    <a class="brand" href="#"><span class="brand-mark"></span><span class="brand-name">Harlow Ridge<br>Junction Railroad</span></a>
    <p class="tagline">A Free Railroad Emergency Contact</p>
    <div class="call">
      <svg width="44" height="44" viewBox="0 0 44 44" aria-hidden="true"><circle cx="22" cy="22" r="20" fill="none" stroke="#e8252f" stroke-width="2.5"/><path d="M15 13c2-1 3 0 4 3l-1 3c1 3 3 5 6 6l3-1c3 1 4 2 3 4-1 2-3 3-5 2-6-2-10-6-12-12-1-2 0-4 2-5z" fill="#e8252f"/></svg>
      <div><div class="call-label">GIVE US A CALL</div><div class="call-number">012-345-6789</div></div>
    </div>
  </div>
</header>

<nav class="main-nav">
  <ul><li>Home</li><li>About Us</li><li>Our Services</li><li>News</li><li>Our Partners</li><li>Contact Us</li></ul>
</nav>

<section class="hero" role="img" aria-label="Steam locomotive with smoke travelling through green trees">
  <span class="hero-arrow" style="left:28px"><svg width="16" height="16" viewBox="0 0 16 16"><path d="M11 2 5 8l6 6" fill="none" stroke="#fff" stroke-width="3"/></svg></span>
  <span class="hero-arrow" style="right:28px"><svg width="16" height="16" viewBox="0 0 16 16"><path d="m5 2 6 6-6 6" fill="none" stroke="#fff" stroke-width="3"/></svg></span>
  <div class="hero-copy">
    <h1>SHORT LINE RAIL ROAD</h1>
    <p>At vero eos et accusamus et iusto odio dignissimos ducimus qui blanditiis praesentium voluptatum deleniti atque corrupti quos dolores et quas molestias excepturi sint.</p>
    <a class="btn" href="#">Read More &raquo;</a>
  </div>
</section>

<section class="welcome">
  <div class="wrap">
    <div class="welcome-copy">
      <h2>Welcome to Our Website!</h2>
      <p class="lead">At vero eos et accusamus et iusto odio dignissimos ducimus qui blanditiis</p>
      <p>Nam libero tempore, cum soluta nobis est eligendi optio cumque nihil impedit quo minus id quod maxime placeat facere possimus, omnis voluptas assumenda est, omnis dolor repellendus. Temporibus autem quibusdam et aut officiis debitis aut rerum necessitatibus saepe eveniet ut et voluptates repudiandae sint et molestiae non recusandae. Itaque earum rerum hic tenetur a sapiente delectus, ut aut reiciendis voluptatibus.</p>
      <a class="btn" href="#">Read More &raquo;</a>
    </div>
    <div class="welcome-photo" role="img" aria-label="Train crossing a green mountain valley"></div>
  </div>
</section>

<section class="services">
  <div class="wrap">
    <h2 class="section-title">Our Services</h2>
    <span class="slide-toggle"></span>
    <div class="service-grid">
      <article class="service-card"><div class="service-photo" role="img" aria-label="Red electric locomotive on tracks" style="background:linear-gradient(#b9c9d6,#8a9a7c 60%,#6b5a4a)"></div><h3>New Rail Customers</h3><p>Neque porro quisquam est, qui dolorem ipsum quia dolor sit amet, consectetur, adipisci velit.</p><a class="btn btn-sm" href="#">View More &raquo;</a></article>
      <article class="service-card"><div class="service-photo" role="img" aria-label="Business handshake" style="background:linear-gradient(135deg,#5a5e66,#2c2f36)"></div><h3>Regional Partners</h3><p>Neque porro quisquam est, qui dolorem ipsum quia dolor sit amet, consectetur, adipisci velit.</p><a class="btn btn-sm" href="#">View More &raquo;</a></article>
      <article class="service-card"><div class="service-photo" role="img" aria-label="Person balancing above a city skyline" style="background:linear-gradient(#c9ccd0,#8d9094 70%,#5d6064)"></div><h3>Development Agencies</h3><p>Neque porro quisquam est, qui dolorem ipsum quia dolor sit amet, consectetur, adipisci velit.</p><a class="btn btn-sm" href="#">View More &raquo;</a></article>
      <article class="service-card"><div class="service-photo" role="img" aria-label="Government office towers against the sky" style="background:linear-gradient(#9fc3e6,#7c8d9e 60%,#6c6258)"></div><h3>Government Regulators</h3><p>Neque porro quisquam est, qui dolorem ipsum quia dolor sit amet, consectetur, adipisci velit.</p><a class="btn btn-sm" href="#">View More &raquo;</a></article>
    </div>
  </div>
</section>

<section class="info-row">
  <div class="wrap">
    <div class="emergency">
      <h2>Emergency Instruction</h2>
      <p class="intro">Nemo enim ipsam voluptatem quia voluptas sit aspernatur aut odit aut fugit, sed quia consequuntur magni dolores eos qui ratione voluptatem sequi nesciunt.</p>
      <div class="emergency-body">
        <div class="emergency-illustration" role="img" aria-label="Emergency exit sign illustration on a yellow wall"></div>
        <div>
          <p>Nam libero tempore, cum soluta nobis est eligendi optio cumque nihil impedit quo minus id quod maxime placeat facere possimus, omnis voluptas assumenda est, omnis dolor repellendus.</p>
          <p>Excepteur sint occaecat cupidatat non proident, sunt in culpa qui officia deserunt mollit.</p>
        </div>
      </div>
    </div>
    <div class="gallery">
      <h2>Our Gallery</h2>
      <p class="intro">Temporibus autem quibusdam et aut officiis debitis aut rerum</p>
      <div class="gallery-grid" role="img" aria-label="Six railway photographs: tracks, trains and landscapes">
        <span style="background:linear-gradient(#7fa65a,#9a6b4a)"></span>
        <span style="background:linear-gradient(#c9d3dc,#b23a3a 60%,#7d8a6a)"></span>
        <span style="background:linear-gradient(#d9d6cf,#8f8a80)"></span>
        <span style="background:linear-gradient(#6f9fd4,#6f9a55)"></span>
        <span style="background:linear-gradient(#8aa7c4,#4f6f3f)"></span>
        <span style="background:linear-gradient(#b5c9d8,#6f8a3f)"></span>
      </div>
    </div>
  </div>
</section>

<section class="map-band" role="img" aria-label="Relief map of the railroad and surrounding area">
  <div class="map-link">
    <div class="pin"><svg width="26" height="30" viewBox="0 0 26 30"><path d="M13 1C7 1 3 5 3 11c0 7 10 18 10 18s10-11 10-18C23 5 19 1 13 1z" fill="#e8252f"/><circle cx="13" cy="11" r="4" fill="#fff"/></svg></div>
    View Our Map
  </div>
</section>

<section class="partners">
  <h2 class="section-title">Our Partners</h2>
  <div class="partner-row">
    <span class="partner-arrow" style="left:-2px">&#8249;</span>
    <span></span>
    <span class="partner" role="img" aria-label="Fenwick County Washington" style="background:#d8cfa0"></span>
    <span class="partner" role="img" aria-label="Port of Merriton (Washington)" style="background:#d9a3a8"></span>
    <span class="partner square" role="img" aria-label="LNPGA"></span>
    <span class="partner" role="img" aria-label="City of Hollow Brook" style="background:#c7cdd6"></span>
    <span class="partner" role="img" aria-label="National Trackway Bureau" style="background:#a9c0de"></span>
    <span class="partner square" role="img" aria-label="MBQ" style="width:230px"></span>
    <span></span>
    <span class="partner-arrow" style="right:-2px">&#8250;</span>
  </div>
</section>

<footer class="site-footer">
  <div class="wrap">
    <div>
      <h4><svg width="14" height="14" viewBox="0 0 14 14"><path d="M5 9l4-4M6 3l2-2a3 3 0 0 1 4 4l-2 2M8 11l-2 2a3 3 0 0 1-4-4l2-2" fill="none" stroke="#fff" stroke-width="1.6"/></svg>Quick Links</h4>
      <ul><li>Home</li><li>About Us</li><li>Our Services</li><li>news</li><li>Our Partners</li><li>Contact Us</li></ul>
    </div>
    <div>
      <h4><svg width="18" height="14" viewBox="0 0 18 14"><rect x="1" y="2" width="10" height="8" fill="#fff"/><path d="M11 5h4l2 3v2h-6z" fill="#fff"/><circle cx="4" cy="11" r="2" fill="#fff"/><circle cx="14" cy="11" r="2" fill="#fff"/></svg>Emergency Contact</h4>
      <div class="field">Your Name:</div>
      <div class="field">Your Email:</div>
      <div class="submit">SUBMIT</div>
    </div>
    <div>
      <h4><svg width="16" height="14" viewBox="0 0 16 14"><path d="M1 4v9h12V9M8 1h7v7M15 1 7 9" fill="none" stroke="#fff" stroke-width="1.6"/></svg>Follow Us</h4>
      <div class="socials"><span></span><span></span><span></span><span></span><span></span></div>
    </div>
    <div class="contact">
      <h4><svg width="18" height="14" viewBox="0 0 18 14"><path d="M1 5c4-5 12-5 16 0l-3 2-2-2H6L4 7z" fill="#fff"/><rect x="4" y="8" width="10" height="5" fill="#fff"/></svg>Contact Us</h4>
      <ul>
        <li><span>&#9679;</span><span><b>Office:</b> No Street Address, City Address, State, Country</span></li>
        <li><span>&#9646;</span><span><b>Mobile:</b> (0001) 2345 6789</span></li>
        <li><span>&#9635;</span><span><b>Fax:</b> (0001) 2345 6789</span></li>
        <li><span>&#9993;</span><span><b>Mail:</b> Contact@domainname.com</span></li>
      </ul>
    </div>
  </div>
</footer>
<div class="copyright">Harlow Ridge Junction Railroad. &copy; 2016 | Privacy Policy</div>

</body>
</html>
```